Lou Brennigan Party invite for 8/20/2018

Lou Brennigan is returning to downtown Jacksonport for another night of fun at Twelve Bells Tavern. Bring a date and tell your friends! Monday, August 20, 2018.
The party starts at 7 pm with limo rides home starting at 11:30.

Target Market(s)

our friends- we will be mailing out this invite

Colors

Designer to choose colors to be used in the design.

Requirements
Must have
• 2 sided postcard for mailing invite
Nice to have
• fun party layout- use the images provides and whatever else you think

```html
<!DOCTYPE html>
<html lang="en">
<head>
<meta charset="utf-8">
<title>Lou Brennigan – Party Invite Postcard</title>
<link href="https://fonts.googleapis.com/css2?family=Playball&family=Lato:wght@400;700;900&display=swap" rel="stylesheet">
<style>
  :root {
    --backdrop: #e6e7e9;
    --card-white: #ffffff;
    --card-grey: #d9d9da;
    --invite-red: #d3262b;
    --invite-red-text: #e0242a;
    --ink: #111111;
    --text-white: #ffffff;
    --photo-dark: #1d1a17;
    --photo-warm: #9a6a3c;
  }
  * { margin: 0; padding: 0; box-sizing: border-box; }
  html, body { width: 1200px; height: 511px; overflow: hidden; }
  body {
    background: var(--backdrop);
    position: relative;
    font-family: "Lato", Arial, sans-serif;
  }
  .postcard {
    position: absolute;
    top: 51px;
    width: 532px;
    height: 410px;
    overflow: hidden;
  }
  .postcard--front { left: 48px; }
  .postcard--back {
    left: 620px;
    background: linear-gradient(90deg, var(--card-grey) 0%, var(--card-white) 45%, var(--card-white) 100%);
  }
  .postcard svg.layer { position: absolute; inset: 0; }
  .text {
    position: absolute;
    left: 0;
    width: 100%;
    text-align: center;
    line-height: 1;
    white-space: nowrap;
  }
  .front-copy { position: absolute; left: 230px; width: 272px; top: 0; height: 100%; color: var(--text-white); }
  .back-copy { position: absolute; left: 40px; width: 228px; top: 0; height: 100%; color: var(--ink); }
  .headliner {
    font-family: "Playball", cursive;
    font-weight: 400;
  }
  .headliner--first { font-size: 72px; }
  .headliner--last { font-size: 58px; }
  .front-copy .headliner { text-shadow: 0 2px 3px rgba(0,0,0,0.25); }
  .back-copy .headliner { text-shadow: 0 2px 3px rgba(0,0,0,0.2); }
  .lead { font-size: 17px; font-weight: 400; }
  .strong { font-size: 17px; font-weight: 700; }
  .rule { position: absolute; height: 2px; }
  .front-copy .rule { background: var(--text-white); left: 30px; width: 212px; }
  .back-copy .rule { background: var(--ink); left: 10px; width: 208px; }
  .details { font-size: 15px; font-weight: 700; line-height: 20px; }
  .cta { color: var(--invite-red-text); font-size: 14px; font-weight: 700; }
  .cta-date { color: var(--invite-red-text); font-size: 17px; font-weight: 900; }
  .stamp-box {
    position: absolute; left: 430px; top: 35px; width: 73px; height: 74px;
    border: 1.5px solid var(--ink);
  }
  .address-line {
    position: absolute; left: 290px; width: 212px; height: 1.5px; background: var(--ink);
  }
</style>
</head>
<body>

<section class="postcard postcard--front">
  <svg class="layer" width="532" height="410" viewBox="0 0 532 410" role="img" aria-label="Photo of a singer with a guitar performing on an outdoor wooden stage at dusk, audience in the foreground">
    <defs>
      <linearGradient id="photo-sky" x1="0" y1="0" x2="0" y2="1">
        <stop offset="0" stop-color="#4a4d5c"/>
        <stop offset="0.35" stop-color="#1f1d1c"/>
        <stop offset="1" stop-color="#181512"/>
      </linearGradient>
      <radialGradient id="photo-stage" cx="0.2" cy="0.75" r="0.45">
        <stop offset="0" stop-color="#c99a62"/>
        <stop offset="0.6" stop-color="#7a5534"/>
        <stop offset="1" stop-color="#1d1a17" stop-opacity="0"/>
      </radialGradient>
    </defs>
    <rect width="532" height="410" fill="url(#photo-sky)"/>
    <rect width="532" height="410" fill="url(#photo-stage)"/>
  </svg>

  <svg class="layer" width="532" height="410" viewBox="0 0 532 410" aria-hidden="true">
    <polygon points="230,0 502,0 502,253 366,317 230,253" fill="var(--invite-red)" opacity="0.9"/>
    <polygon points="230,303 366,362 502,303 502,410 230,410" fill="#ffffff" opacity="0.85"/>
  </svg>

  <div class="front-copy">
    <div class="text headliner headliner--first" style="top:36px;">Lou</div>
    <div class="text headliner headliner--last" style="top:108px;">Brennigan</div>
    <div class="text lead" style="top:195px;">is returning to downtown</div>
    <div class="text strong" style="top:214px;">JACKSONPORT</div>
    <div class="rule" style="top:241px;"></div>
    <div class="text lead" style="top:257px;">Another Night Of Fun At</div>
    <div class="text strong" style="top:281px;">Twelve Bells Tavern</div>
    <div class="text cta" style="top:357px;">Bring a date and tell your friends!</div>
    <div class="text cta-date" style="top:376px;">Monday, August 20, 2018.</div>
  </div>
</section>

<section class="postcard postcard--back">
  <div class="back-copy">
    <div class="text headliner headliner--first" style="top:24px;">Lou</div>
    <div class="text headliner headliner--last" style="top:100px;">Brennigan</div>
    <div class="text lead" style="top:218px;">is returning to downtown</div>
    <div class="text strong" style="top:241px;">JACKSONPORT</div>
    <div class="rule" style="top:265px;"></div>
    <div class="text lead" style="top:281px;">Another Night Of Fun At</div>
    <div class="text strong" style="top:305px;">Twelve Bells Tavern</div>
    <div class="rule" style="top:330px;"></div>
    <div class="text details" style="top:337px;">Party starts at 7 pm with<br>limo rides home starting<br>at 11:30.</div>
  </div>
  <div class="stamp-box"></div>
  <div class="address-line" style="top:254px;"></div>
  <div class="address-line" style="top:302px;"></div>
  <div class="address-line" style="top:350px;"></div>
</section>

</body>
</html>
```